Creative Consulting Company
business card, stationary, ppt template
Creative Consulting Company - Communications and Media
Creative Brief
Use specific fonts
Use what works the best in your design
Professional
Till Molnar
CEO
Molnar Communications GmbH Tannwaldstrasse 87 CH-8999 Zurich
till.molnar@molnarkom-demo.ch
www.molnarkom-demo.ch
Molnar Communications is a consultancy that specializes in all aspects of high end event organization and sponsorship activation. We are located in Switzerland. I'm looking for a clean and stylish look. The sizes are european: Letterhead: DIN A4 210mm x 297mm (8.27" x 11.69") Business Cards: 85mm x 54mm (3.346" x 2.126") Plz use "Mobile" instead of "Cell" Stationery: --------------- Do not use Ilustration which runs off the edge. We do print the letters with our own printers. Therefore, there will be a margin. And please no watermarks. Business Cards: ----------------------- I consider to grade up the back of the card with some varnish or film, but not sure yet. You can use either the black or the white logo. ppt Template: ------------------ Template should match the grafical concept.
Just the Logo. I you mind pimp up the logo a little bit (gradient, shadow, 3D etc.), feel free to do so. But you don't have to.

```html
<!DOCTYPE html>
<html lang="en">
<head>
<meta charset="utf-8">
<title>Molnar Communications – Stationery Set</title>
<link rel="stylesheet" href="https://fonts.googleapis.com/css2?family=Montserrat:wght@500&family=Open+Sans:wght@400;600&display=swap">
<style>
  :root {
    --backdrop: #9c9c9c;
    --paper: #ffffff;
    --ink: #3b3b3b;
    --ink-soft: #555555;
    --text-small: #4a4a4a;
  }
  * { box-sizing: border-box; margin: 0; padding: 0; }
  html, body { width: 1200px; height: 684px; overflow: hidden; }
  body {
    background: var(--backdrop);
    font-family: "Open Sans", Arial, sans-serif;
    color: var(--text-small);
    position: relative;
  }
  .piece { position: absolute; background: var(--paper); overflow: hidden; box-shadow: 0 1px 3px rgba(0,0,0,.18); }

  /* wordmark: invented name set in the text font, one plain square beside it */
  .wordmark {
    position: absolute; left: 0; right: 0;
    display: flex; justify-content: center; align-items: center; gap: .45em;
    font-family: "Montserrat", Arial, sans-serif;
    font-weight: 500;
    line-height: 1;
    white-space: nowrap;
  }
  .wordmark-square { width: .7em; height: .7em; background: currentColor; flex: none; }
  .wordmark--dark { color: var(--ink); }
  .wordmark--light { color: var(--paper); }

  .fine { position: absolute; left: 0; right: 0; text-align: center; line-height: 1; white-space: nowrap; }

  /* business card front */
  .card-front { left: 31px; top: 228px; width: 197px; height: 110px; background: var(--ink); }
  .card-front .wordmark { top: 49px; font-size: 12px; }

  /* business card back */
  .card-back { left: 31px; top: 343px; width: 197px; height: 113px; }
  .card-back .holder { top: 10px; font-size: 5px; font-weight: 600; color: var(--ink); }
  .card-back .role { top: 17px; font-size: 4px; }
  .card-back .wordmark { top: 48px; font-size: 10px; }
  .card-back .contact-1 { top: 90px; font-size: 4px; }
  .card-back .contact-2 { top: 97px; font-size: 4px; }

  /* letterhead */
  .letterhead { left: 252px; top: 36px; width: 348px; height: 612px; }
  .letterhead .band { position: absolute; left: 0; right: 0; top: 7px; height: 34px; background: var(--ink); }
  .letterhead .rule { position: absolute; left: 0; right: 0; top: 48px; height: 2px; background: var(--ink-soft); }
  .letterhead .wordmark { top: 70px; font-size: 12px; }
  .letterhead .web { top: 581px; font-size: 5px; font-weight: 600; }
  .letterhead .address { top: 592px; font-size: 4.5px; }

  /* envelope back */
  .envelope-back { left: 643px; top: 96px; width: 533px; height: 228px; }
  .envelope-back .flap { position: absolute; left: 0; top: 0; }
  .envelope-back .wordmark { top: 44px; font-size: 12px; }

  /* envelope front */
  .envelope-front { left: 643px; top: 372px; width: 533px; height: 240px; }
  .envelope-front .band { position: absolute; left: 0; right: 0; top: 5px; height: 36px; background: var(--ink); }
  .envelope-front .rule { position: absolute; left: 0; right: 0; top: 44px; height: 2px; background: var(--ink-soft); }
  .envelope-front .wordmark { top: 70px; font-size: 13px; }
  .envelope-front .web { top: 197px; font-size: 5px; font-weight: 600; }
  .envelope-front .address { top: 207px; font-size: 4.5px; }
</style>
</head>
<body>

  <section class="piece card-front">
    <div class="wordmark wordmark--light"><span class="wordmark-square"></span><span>Molnar Communications</span></div>
  </section>

  <section class="piece card-back">
    <p class="fine holder">Till Molnar</p>
    <p class="fine role">CEO</p>
    <div class="wordmark wordmark--dark"><span class="wordmark-square"></span><span>Molnar Communications</span></div>
    <p class="fine contact-1">Molnar Communications GmbH · Tannwaldstrasse 87 · CH-8999 Zurich</p>
    <p class="fine contact-2">Mobile: +41 79 000 00 00 · till.molnar@molnarkom-demo.ch</p>
  </section>

  <section class="piece letterhead">
    <div class="band"></div>
    <div class="rule"></div>
    <div class="wordmark wordmark--dark"><span class="wordmark-square"></span><span>Molnar Communications</span></div>
    <p class="fine web">www.molnarkom-demo.ch</p>
    <p class="fine address">Molnar Communications GmbH · Tannwaldstrasse 87 · CH-8999 Zurich · Mobile: +41 79 000 00 00 · Email: till.molnar@molnarkom-demo.ch</p>
  </section>

  <section class="piece envelope-back">
    <svg class="flap" width="533" height="134" viewBox="0 0 533 134">
      <path d="M0 0 H533 V70 Q533 132 470 132 H63 Q0 132 0 70 Z" fill="#3b3b3b"/>
    </svg>
    <div class="wordmark wordmark--light"><span class="wordmark-square"></span><span>Molnar Communications</span></div>
  </section>

  <section class="piece envelope-front">
    <div class="band"></div>
    <div class="rule"></div>
    <div class="wordmark wordmark--dark"><span class="wordmark-square"></span><span>Molnar Communications</span></div>
    <p class="fine web">www.molnarkom-demo.ch</p>
    <p class="fine address">Molnar Communications GmbH · Tannwaldstrasse 87 · CH-8999 Zurich · Mobile: +41 79 000 00 00 · Email: till.molnar@molnarkom-demo.ch</p>
  </section>

</body>
</html>
```